Layout for site fence advertising - length approx. 250 cm x 125 cm

The advertising will later be printed on a PVC film and used for events or on sports fields.

Main services :
Your regional contact at
Real estate and business financing
independent insurance advice

```html
<!DOCTYPE html>
<html lang="de">
<head>
<meta charset="utf-8">
<title>Kovar Finanzberatung – Bauzaunbanner</title>
<link rel="stylesheet" href="https://fonts.googleapis.com/css2?family=Nunito:wght@700;800&family=Quicksand:wght@600;700&display=swap">
<style>
  :root {
    --brand-blue: #2b58ad;
    --ink-grey: #4a4a4c;
    --phone-box: #5e5e62;
    --page-bg: #f3f2f4;
    --sky-top: #eef1f5;
    --city-mid: #bcc6cf;
    --field-green: #a9b39a;
    --white: #ffffff;
  }
  * { box-sizing: border-box; margin: 0; padding: 0; }
  html, body {
    width: 1050px;
    height: 1200px;
    overflow: hidden;
    background: var(--page-bg);
  }
  .banner {
    position: absolute;
    left: 25px;
    top: 350px;
    width: 1000px;
    height: 500px;
    overflow: hidden;
    box-shadow: 4px 6px 12px rgba(0,0,0,0.35);
  }
  .banner__backdrop {
    position: absolute;
    inset: 0;
    background: linear-gradient(180deg, var(--sky-top) 0%, #e3e8ee 26%, var(--city-mid) 45%, #c3c8c4 68%, var(--field-green) 100%);
    opacity: 0.85;
  }
  .banner__ring {
    position: absolute;
    left: 0;
    top: 0;
    width: 1000px;
    height: 500px;
  }
  .phone-tag {
    position: absolute;
    left: 78px;
    top: 407px;
    width: 347px;
    height: 55px;
    border: 1px solid var(--white);
  }
  .phone-tag__box {
    position: absolute;
    left: 10px;
    top: 7px;
    width: 327px;
    height: 41px;
    background: var(--phone-box);
    display: flex;
    align-items: center;
    justify-content: center;
  }
  .phone-tag__number {
    font-family: 'Nunito', sans-serif;
    font-weight: 800;
    font-size: 31px;
    color: var(--white);
    letter-spacing: 0.5px;
  }
  .brand {
    position: absolute;
    left: 515px;
    top: 23px;
    height: 127px;
    display: flex;
    align-items: center;
  }
  .brand__dot {
    width: 118px;
    height: 118px;
    border: 3px solid var(--brand-blue);
    border-radius: 50%;
    margin-right: 14px;
  }
  .brand__divider {
    width: 3px;
    height: 127px;
    background: var(--ink-grey);
    margin-right: 10px;
  }
  .brand__name {
    font-family: 'Quicksand', sans-serif;
    font-weight: 700;
    font-size: 23px;
    color: var(--brand-blue);
    line-height: 1.1;
  }
  .brand__tagline {
    font-family: 'Quicksand', sans-serif;
    font-weight: 600;
    font-size: 16px;
    color: var(--ink-grey);
    margin-top: 8px;
  }
  .services {
    position: absolute;
    left: 520px;
    width: 440px;
    top: 208px;
    text-align: center;
    font-family: 'Nunito', sans-serif;
    font-weight: 800;
    font-size: 35px;
    line-height: 50px;
    color: var(--brand-blue);
    letter-spacing: -0.5px;
    text-shadow:
      2px 0 0 var(--white), -2px 0 0 var(--white),
      0 2px 0 var(--white), 0 -2px 0 var(--white),
      1.5px 1.5px 0 var(--white), -1.5px 1.5px 0 var(--white),
      1.5px -1.5px 0 var(--white), -1.5px -1.5px 0 var(--white);
  }
</style>
</head>
<body>
  <section class="banner">
    <div class="banner__backdrop" role="img" aria-label="Aerial view of a city by a river with vineyards and fields in the foreground"></div>

    <svg class="banner__ring" viewBox="0 0 1000 500" aria-hidden="false">
      <defs>
        <linearGradient id="portraitFill" x1="0" y1="0" x2="0" y2="1">
          <stop offset="0" stop-color="#f4f5f7"/>
          <stop offset="0.55" stop-color="#d9dde2"/>
          <stop offset="1" stop-color="#3a3d46"/>
        </linearGradient>
      </defs>
      <circle cx="245" cy="252" r="240" fill="url(#portraitFill)" role="img" aria-label="Portrait photo of the advisor in a dark jacket and white shirt"/>
      <circle cx="245" cy="252" r="243" fill="none" stroke="var(--brand-blue)" stroke-width="5"/>
      <path d="M 462 347 A 243 243 0 0 1 245 495 A 243 243 0 0 1 8 300
               A 248 248 0 0 0 245 470 A 225 225 0 0 0 440 338 Z"
            fill="var(--brand-blue)"/>
    </svg>

    <div class="phone-tag">
      <div class="phone-tag__box">
        <span class="phone-tag__number">+43 660 214 5890</span>
      </div>
    </div>

    <header class="brand">
      <div class="brand__dot"></div>
      <div class="brand__divider"></div>
      <div class="brand__text">
        <p class="brand__name">Kovar Finanzberatung GmbH</p>
        <p class="brand__tagline">Finanzieren, Versichern, Vorsorgen</p>
      </div>
    </header>

    <div class="services">
      <p>Your regional contact at</p>
      <p>REAL ESTATE and</p>
      <p>BUSINESS FINANCING</p>
      <p>independent</p>
      <p>INSURANCE advice</p>
    </div>
  </section>
</body>
</html>
```